MOTOR BOOST MODULE ONLINE SHOP

NEW ECOMMERCE SITE, SELLING TUNING CHIPS FOR VEHICLES -

performance and fuel efficiency tuning for cars, vans, jeeps, agri (tractors harvestors, trucks)

Must be user friendly layout - easy to understand, select product and purchase online.

Product: This is a computer chip which can be purchased by a customer, DIY installed to their vehicle using OEM plugs, for improved performance and fuel efficiency.

IDEAS:

1. KPL WORKS

2. SPEEDLOOM.EXAMPLE

3. GRAVMOTOR.EXAMPLE

NEW BRAND - BQN (MOTOR BOOST MODULE)
NEED A LOGO AND DESIGN IDEAS

Target Market(s)

AUTOMOTIVE SECTORS WORLDWIDE

Industry/Entity Type

Shop

Logo Text

BQN - CHIPTUNING

Number of Pages Required

1 page

Requirements
Must have
• nice layout - section for light vehicles ie. cars/vans . Section for agri vehicles ie. tractors
Nice to have
• KPL WORKS website is very good. GMEX , SPEEDLOOM are also very good to get ideas from.

```html
<!DOCTYPE html>
<html lang="en">
<head>
<meta charset="utf-8">
<title>BQN – Motor Boost Module</title>
<link href="https://fonts.googleapis.com/css2?family=Montserrat:wght@400;500;600;700&family=Open+Sans:wght@400;600&display=swap" rel="stylesheet">
<style>
:root{
  --red:#b5121b;
  --dark:#2b2b2b;
  --darker:#232323;
  --ink:#333;
  --muted:#666;
  --light:#efefef;
  --pale:#f5f5f5;
  --white:#fff;
  --tile:#3d3d3d;
}
*{box-sizing:border-box;margin:0;padding:0}
html,body{width:1200px;height:3072px;overflow:hidden}
body{font-family:"Open Sans",Arial,sans-serif;color:var(--ink);background:var(--white);position:relative}
.wrap{width:934px;margin:0 auto;position:relative;height:100%}
h1,h2,h3,h4,.btn,.tag{font-family:"Montserrat",Arial,sans-serif}
.section-title{text-align:center;font-size:24px;font-weight:600;letter-spacing:.5px;color:#2a2a2a}

/* top bar */
.topbar{height:41px;background:var(--pale);font-size:12px;color:#444}
.topbar .wrap{display:flex;justify-content:space-between;align-items:center}
.topbar span{margin-right:18px;display:inline-flex;align-items:center;gap:6px}
.topbar .right span{margin:0 0 0 24px}

/* header */
.header{height:119px;background:var(--dark)}
.header .wrap{display:flex;justify-content:space-between;align-items:center}
.brand-name{font-family:"Montserrat",sans-serif;font-weight:700;font-size:46px;color:var(--white);line-height:1;letter-spacing:1px}
.brand-tag{font-size:11px;color:#ddd;letter-spacing:.3px;margin-top:4px}
.nav a{color:#ccc;font-size:13px;text-decoration:none;margin-left:24px}
.nav a.active{color:var(--white);border-bottom:1px solid var(--white);padding-bottom:2px}

/* hero */
.hero{height:454px;position:relative;background:linear-gradient(100deg,#8b8d88 0%,#b5b3a9 30%,#d9dde2 55%,#a11a22 68%,#c4c7ca 85%,#5e5f5a 100%)}
.hero-copy{position:absolute;left:131px;top:178px;color:var(--white)}
.hero-copy h1{font-size:33px;line-height:38px;font-weight:700;letter-spacing:.5px}
.btn-white{display:inline-block;margin-top:12px;background:var(--white);color:#222;font-size:12px;font-weight:600;padding:11px 20px}
.hero-arrow{position:absolute;top:372px;width:26px;height:26px;background:rgba(60,60,60,.8);display:flex;align-items:center;justify-content:center}
.hero-arrow.left{left:0}.hero-arrow.right{right:0}

/* vehicle finder */
.finder{height:160px;background:var(--light);padding-top:24px}
.finder .grid{display:flex;gap:8px;margin-top:18px;align-items:flex-end}
.field label{display:block;font-size:12px;color:#444;margin-bottom:6px}
.select{width:217px;height:39px;background:var(--white);border:1px solid #ddd;display:flex;align-items:center;justify-content:space-between;padding:0 14px;font-size:11px;color:#999}
.go{width:31px;height:39px;background:#3a3a3a;margin-left:2px;display:flex;align-items:center;justify-content:center}

/* vehicle panels */
.panels{display:flex;height:455px}
.panel{flex:1;position:relative}
.panel.light{background:linear-gradient(180deg,#3c5a86 0%,#6f7f95 45%,#7a4a2a 70%,#3a2a20 100%)}
.panel.agri{background:linear-gradient(180deg,#4b86c8 0%,#9fc1e3 45%,#a4242c 62%,#6b5444 80%,#4e3d30 100%)}
.panel-copy{position:absolute;left:131px;top:39px;color:var(--white)}
.panel.agri .panel-copy{left:224px}
.tag{display:inline-block;background:var(--red);color:var(--white);font-size:14px;font-weight:600;padding:5px 16px;clip-path:polygon(8px 0,100% 0,calc(100% - 8px) 100%,0 100%)}
.panel-copy h2{font-size:32px;font-weight:600;line-height:36px;margin-top:4px}
.panel-copy p{font-size:12px}

/* how it works */
.how{height:440px;padding-top:76px}
.steps{display:flex;justify-content:space-between;margin-top:26px}
.step{width:330px;text-align:center}
.step .icon{width:88px;height:88px;border-radius:50%;background:#3a3a3a;margin:0 auto;display:flex;align-items:center;justify-content:center}
.step h3{color:var(--red);font-size:15px;font-weight:600;margin-top:22px}
.step p{font-size:10.5px;line-height:17px;color:var(--muted);margin:6px auto 0;width:330px}
.btn{display:inline-block;background:var(--red);color:var(--white);font-size:15px;font-weight:600;padding:6px 22px;clip-path:polygon(8px 0,100% 0,calc(100% - 8px) 100%,0 100%);margin-top:12px}

/* about + features */
.about{height:518px;background:var(--light);padding-top:80px}
.about .cols{display:flex;justify-content:space-between}
.about .col{width:442px}
.col h2{font-size:22px;font-weight:600;color:#2a2a2a}
.col p{font-size:10.5px;line-height:18.5px;color:var(--muted);margin-top:10px;text-align:justify}
.engine{height:176px;margin-top:14px;background:linear-gradient(135deg,#6b6f73,#2e3033 55%,#8d8f90)}
.features{display:flex;gap:6px;margin-top:20px}
.feature{flex:1;height:125px;background:var(--tile);color:#ddd;padding:12px 12px;font-size:10px;line-height:14px}
.feature svg{display:block;margin-bottom:10px}
.clients{height:176px;margin-top:16px;position:relative;background:linear-gradient(90deg,#3b4d66 0%,#6b87a8 55%,#c7b5a3 80%,#5c6e86 100%)}
.clients h3{position:absolute;left:20px;top:22px;color:var(--white);font-size:22px;font-weight:600}
.clients .mini{position:absolute;left:20px;top:58px;background:var(--red);color:var(--white);font-family:"Montserrat",sans-serif;font-size:10px;font-weight:600;padding:5px 14px}

/* products */
.products{height:387px;padding-top:76px}
.product-row{display:flex;justify-content:space-between;margin-top:28px}
.product{width:426px;display:flex;gap:18px}
.product .photo{width:180px;height:180px;border-radius:50%;flex:none}
.product .photo.one{background:radial-gradient(circle at 45% 40%,#6d88a8,#28476d 70%)}
.product .photo.two{background:radial-gradient(circle at 50% 45%,#4d5258,#16181b 70%)}
.product h3{color:var(--red);font-size:15px;font-weight:600;margin-top:14px}
.product p{font-size:10.5px;line-height:17px;color:var(--muted);margin-top:6px;width:228px}
.product .btn{margin-top:12px}

/* awards */
.awards{height:176px;background:#f2f2f2;padding-top:50px}
.awards h4{text-align:center;font-size:12px;font-weight:500;color:#333;letter-spacing:.5px}
.marks{display:flex;justify-content:space-between;align-items:center;margin-top:36px}
.mark{font-family:"Montserrat",sans-serif;font-weight:600;font-size:17px;color:#222}

/* footer */
.footer{height:230px;background:#2e2e2e;color:#ddd;padding-top:36px}
.footer .cols{display:flex}
.footer h4{font-size:15px;font-weight:500;color:#eee;margin-bottom:12px}
.contact-form{width:361px}
.input{width:219px;height:37px;background:var(--white);color:#555;font-size:10px;padding:12px 12px;margin-bottom:5px}
.msg-row{display:flex;gap:6px}
.submit{width:70px;height:37px;background:#666;color:#eee;font-size:11px;display:flex;align-items:center;justify-content:center;font-family:"Montserrat",sans-serif}
.links{width:151px}
.links li{list-style:none;font-size:10px;color:#ccc;line-height:27px}
.info{width:315px}
.info li{list-style:none;font-size:10px;color:#ccc;line-height:24px;display:flex;align-items:center;gap:10px}
.social{display:flex;gap:8px}
.social span{width:25px;height:25px;border-radius:50%;background:#555;display:block}
.copyright{height:92px;background:var(--darker);border-top:1px solid #3a3a3a;text-align:center;font-size:10px;color:#aaa;padding-top:40px}
</style>
</head>
<body>

<div class="topbar">
  <div class="wrap">
    <div>
      <span><svg width="8" height="10" viewBox="0 0 8 10"><rect x="1" y="0" width="6" height="10" rx="1" fill="#555"/></svg>555 010 0148</span>
      <span><svg width="11" height="8" viewBox="0 0 11 8"><rect width="11" height="8" fill="#555"/><path d="M0 0l5.5 4L11 0" stroke="#fff" fill="none"/></svg>info@bqn.example</span>
    </div>
    <div class="right">
      <span><svg width="9" height="10" viewBox="0 0 9 10"><circle cx="4.5" cy="3" r="2.5" fill="#555"/><path d="M0 10c0-3 2-4.5 4.5-4.5S9 7 9 10z" fill="#555"/></svg>My Account</span>
      <span><svg width="11" height="10" viewBox="0 0 11 10"><path d="M0 1h2l2 6h6l1-4H3" stroke="#555" fill="none"/><circle cx="5" cy="9" r="1" fill="#555"/><circle cx="9" cy="9" r="1" fill="#555"/></svg>My Cart - 0 items</span>
    </div>
  </div>
</div>

<header class="header">
  <div class="wrap">
    <div class="brand">
      <div class="brand-name">BQN</div>
      <div class="brand-tag">MOTOR BOOST MODULE</div>
    </div>
    <nav class="nav">
      <a class="active">Home</a><a>About</a><a>Shop</a><a>Chip Tunning</a><a>Support</a>
    </nav>
  </div>
</header>

<section class="hero" role="img" aria-label="Red hatchback driving fast along a country road">
  <div class="hero-copy">
    <h1>PRAESENT IACULIS<br>FAUCIBUS URNA</h1>
    <span class="btn-white">READ MORE</span>
  </div>
  <div class="hero-arrow left"><svg width="8" height="10"><path d="M7 0L1 5l6 5z" fill="#fff"/></svg></div>
  <div class="hero-arrow right"><svg width="8" height="10"><path d="M1 0l6 5-6 5z" fill="#fff"/></svg></div>
</section>

<section class="finder">
  <div class="wrap">
    <h2 class="section-title">CHOOSE YOUR VEHICLE</h2>
    <div class="grid">
      <div class="field"><label>Manufacturer</label><div class="select">Select<svg width="9" height="5"><path d="M0 0h9L4.5 5z" fill="#555"/></svg></div></div>
      <div class="field"><label>Model</label><div class="select">Select<svg width="9" height="5"><path d="M0 0h9L4.5 5z" fill="#555"/></svg></div></div>
      <div class="field"><label>Engine</label><div class="select">Select<svg width="9" height="5"><path d="M0 0h9L4.5 5z" fill="#555"/></svg></div></div>
      <div class="field"><label>Type</label><div class="select">Car<svg width="9" height="5"><path d="M0 0h9L4.5 5z" fill="#555"/></svg></div></div>
      <div class="go"><svg width="9" height="12"><path d="M1 0l7 6-7 6z" fill="#fff"/></svg></div>
    </div>
  </div>
</section>

<section class="panels">
  <div class="panel light" role="img" aria-label="Bronze saloon car on an open road at dusk">
    <div class="panel-copy"><span class="tag">CHIP FOR</span><h2>LIGHT VEHICLES</h2><p>(Cars, Vans)</p></div>
  </div>
  <div class="panel agri" role="img" aria-label="Red tractor pulling a cultivator across a ploughed field">
    <div class="panel-copy"><span class="tag">CHIP FOR</span><h2>AGRI VEHICLES</h2><p>(Tractors )</p></div>
  </div>
</section>

<section class="how">
  <div class="wrap">
    <h2 class="section-title">HOW IT WORKS</h2>
    <div class="steps">
      <div class="step">
        <div class="icon"><svg width="34" height="38" viewBox="0 0 34 38"><path d="M3 12h28l-2 24H5z" fill="#fff"/><path d="M11 14V8a6 6 0 0112 0v6" stroke="#fff" stroke-width="2.5" fill="none"/></svg></div>
        <h3>ORDER OUR CHIP HERE</h3>
        <p>Phasellus nisl est, condimentum vitae faucibus in, sollicitudin vel metus. Nunc sit amet consequat risus. Curabitur ac elit leo. In eleifend dui tellus, in scelerisque</p>
        <span class="btn">ORDER NOW</span>
      </div>
      <div class="step">
        <div class="icon"><svg width="42" height="28" viewBox="0 0 42 28"><path d="M4 14l5-11h24l5 11v10H4z" fill="#fff"/><rect x="11" y="6" width="20" height="7" fill="#3a3a3a"/><circle cx="11" cy="19" r="3" fill="#3a3a3a"/><circle cx="31" cy="19" r="3" fill="#3a3a3a"/></svg></div>
        <h3>DIY INSTALLED USING OEM PLUGS</h3>
        <p>Phasellus nisl est, condimentum vitae faucibus in, sollicitudin vel metus. Nunc sit amet consequat risus. Curabitur ac elit leo. In eleifend dui tellus, in scelerisque</p>
        <span class="btn">LEARN MORE</span>
      </div>
      <div class="step">
        <div class="icon"><svg width="40" height="40" viewBox="0 0 40 40"><circle cx="20" cy="20" r="18" fill="#fff"/><path d="M6 20a14 14 0 0128 0z" fill="#3a3a3a"/><path d="M20 20l8-9" stroke="#b5121b" stroke-width="3"/><circle cx="20" cy="20" r="3" fill="#b5121b"/></svg></div>
        <h3>GET IMPROVED PERFORMANCE</h3>
        <p>Phasellus nisl est, condimentum vitae faucibus in, sollicitudin vel metus. Nunc sit amet consequat risus. Curabitur ac elit leo. In eleifend dui tellus, in scelerisque</p>
        <span class="btn">LEARN MORE</span>
      </div>
    </div>
  </div>
</section>

<section class="about">
  <div class="wrap">
    <div class="cols">
      <div class="col">
        <h2>ABOUT OUR CHIP</h2>
        <p>Fusce sollicitudin lorem et luctus volutpat. Proin placerat dapibus gravida. In tristique tristique nulla eget hendrerit. Maecenas vel tortor accumsan quam varius imperdiet vel eget elit. Aenean facilisis tincidunt lectus, id dictum nisi luctus eget. Vivamus efficitur ex condimentum, malesuada eros eget, feugiat nibh. Sed tellus ex, imperdiet eget gravida sit amet, volutpat eget turpis. In nec ultricies est. Etiam mattis augue vehicula odio posuere, sit amet tempus lectus luctus. Nulla facilisi. Etiam vel massa elementum, bibendum tellus venenatis, feugiat massa.</p>
        <div class="engine" role="img" aria-label="Close view of a car engine bay under an open bonnet"></div>
      </div>
      <div class="col">
        <h2>FEATURES</h2>
        <div class="features">
          <div class="feature"><svg width="16" height="16" viewBox="0 0 16 16"><path d="M2 14l7-7M10 2a4 4 0 104 4l-2 1-3-3z" stroke="#fff" stroke-width="2" fill="none"/></svg>Aenean placerat, nibh vel accumsan aliquet, magna nibh accumsan nibh, ac tempus num.</div>
          <div class="feature"><svg width="16" height="16" viewBox="0 0 16 16"><circle cx="8" cy="8" r="5" stroke="#fff" stroke-width="3" stroke-dasharray="3 2" fill="none"/><circle cx="8" cy="8" r="2" fill="#fff"/></svg>Phasellus nisl est, condimentum vitae faucibus in, sollicitudin vel metus amet consequat risus.</div>
          <div class="feature"><svg width="12" height="16" viewBox="0 0 12 16"><path d="M6 0C4 5 1 8 1 11a5 5 0 0010 0C11 8 8 5 6 0z" fill="#fff"/></svg>Maecenas vel tortor accumsan quam varius imperdiet vel eget elit tincidunt lectus.</div>
        </div>
        <div class="clients" role="img" aria-label="Smiling customer holding car keys beside his vehicle">
          <h3>HAPPY CLIENTS</h3>
          <span class="mini">VIEW OUR CLIENTS TESTIMONIALS</span>
        </div>
      </div>
    </div>
  </div>
</section>

<section class="products">
  <div class="wrap">
    <h2 class="section-title">OUR PRODUCTS</h2>
    <div class="product-row">
      <div class="product">
        <div class="photo one" role="img" aria-label="Mechanic with a laptop in a workshop"></div>
        <div>
          <h3>NULLA TRISTIQUE POSUERE</h3>
          <p>Phasellus nisl est, condimentum vitae faucibus in, sollicitudin vel metus. Nunc sit amet consequat risus. Curabitur ac elit leo. In eleifend dui tellus, in scelerisque</p>
          <span class="btn">ORDER NOW</span>
        </div>
      </div>
      <div class="product">
        <div class="photo two" role="img" aria-label="Tablet showing engine diagnostics held over a steering wheel"></div>
        <div>
          <h3>PELLENTESQUE CONVALLIS</h3>
          <p>Phasellus nisl est, condimentum vitae faucibus in, sollicitudin vel metus. Nunc sit amet consequat risus. Curabitur ac elit leo. In eleifend dui tellus, in scelerisque</p>
          <span class="btn">ORDER NOW</span>
        </div>
      </div>
    </div>
  </div>
</section>

<section class="awards">
  <div class="wrap">
    <h4>AWARDS &amp; PRICINGS</h4>
    <div class="marks">
      <span class="mark">QUORVEL</span><span class="mark">Halvrin</span><span class="mark">ZEMBRIK</span><span class="mark">TOLVANE</span><span class="mark">nuvesca</span><span class="mark">YXORA</span><span class="mark">PRAVELD</span>
    </div>
  </div>
</section>

<footer class="footer">
  <div class="wrap">
    <div class="cols">
      <div class="contact-form">
        <h4>Contact Us</h4>
        <div class="input">Name</div>
        <div class="input">Email</div>
        <div class="msg-row"><div class="input">Message</div><div class="submit">SUBMIT</div></div>
      </div>
      <div class="links">
        <h4>Links</h4>
        <ul><li>› Home</li><li>› About</li><li>› Shop</li><li>› Chip Tunning</li><li>› Support</li></ul>
      </div>
      <div class="info">
        <h4>Contact Info</h4>
        <ul>
          <li><svg width="8" height="11" viewBox="0 0 8 11"><path d="M4 0a4 4 0 014 4c0 3-4 7-4 7S0 7 0 4a4 4 0 014-4z" fill="#bbb"/></svg>24 Building name, Street name, City - Zipcode</li>
          <li><svg width="8" height="11" viewBox="0 0 8 11"><rect x="1" width="6" height="11" rx="1" fill="#bbb"/></svg>555 010 0265</li>
          <li><svg width="10" height="8" viewBox="0 0 10 8"><rect width="10" height="8" fill="#bbb"/><path d="M0 0l5 4 5-4" stroke="#2e2e2e" fill="none"/></svg>info@bqn.example</li>
        </ul>
      </div>
      <div class="follow">
        <h4>Follow us on</h4>
        <div class="social"><span aria-label="Social link one"></span><span aria-label="Social link two"></span><span aria-label="Social link three"></span></div>
      </div>
    </div>
  </div>
</footer>
<div class="copyright">Copyright © 2017 BQN. All rights reserved.</div>

</body>
</html>
```